New Woocommerce Design Project

We need a WooCommerce site design that reflects our personality as a young and stylish teenage 'athleisure' fashion brand. Our target market is young boys aged between 12 and 18 years old, who are sporty, cool, and fashion conscious. We would like to the site to feature large format photos of our products and models, as well as feature pages for product selection for purchase. This is a new company we are launching, so we are looking for a dynamic yet stylish design which is quick and easy to navigate and which will appeal to young people. We already have a logo which we will upload below. Our existing domain name is www.orbitwren.com. We would like the winning designer to code the website - if possible. We have uploaded some photos of the products currently being manufactured so you can see the type of design/style.

Target Market(s)

Teenage boys

Industry/Entity Type

Fashion

Coding

Coded - Design and coding required

Colors

Designer to choose colors to be used in the design.

Requirements
Must have
• Inclusion of logo, design must be stylish and contemporary. Colours must include white, logo background colour, and a dark navy blue.
Nice to have
• Inclusion of whole page photos of possible
Should not have
• Nothing that looks cheap or too childish.

```html
<!DOCTYPE html>
<html lang="en">
<head>
<meta charset="utf-8">
<title>Orbit Wren — Athleisure for Boys</title>
<link rel="stylesheet" href="https://fonts.googleapis.com/css2?family=Abril+Fatface&family=Roboto:wght@400;500;700&display=swap">
<style>
:root{
  --taupe:#9b8c80;
  --navy:#1b1b6e;
  --ink:#111;
  --pale:#f3f6fc;
  --yellow:#f0b323;
  --slate:#2a2d3e;
  --grey-blue:#c3ccd4;
  --star:#f4b400;
  --muted:#555;
  --white:#fff;
}
*{box-sizing:border-box;margin:0;padding:0}
html,body{width:1200px;height:4367px;overflow:hidden}
body{position:relative;font-family:"Roboto",sans-serif;color:var(--ink);background:var(--white)}
.abs{position:absolute}
.serif{font-family:"Abril Fatface",serif;font-weight:400}
.btn{position:absolute;background:var(--ink);color:var(--white);font-family:"Abril Fatface",serif;font-size:15px;display:flex;align-items:center;justify-content:center;letter-spacing:.3px}
.ph{position:absolute}

.topbar{position:absolute;left:0;top:0;width:1200px;height:50px;background:var(--taupe)}
.social{position:absolute;top:14px;width:24px;height:24px;border:1.5px solid var(--white);border-radius:50%}
.account{position:absolute;right:103px;top:17px;color:var(--white);font-size:14px;font-weight:500;display:flex;gap:7px;align-items:center}

.header{position:absolute;left:0;top:50px;width:1200px;height:89px;background:var(--white)}
.logo-tab{position:absolute;left:505px;top:32px;width:190px;height:106px;background:var(--white);border-radius:40px 40px 0 0}
.brand{position:absolute;left:505px;top:100px;width:190px;text-align:center;font-size:22px;letter-spacing:5px;color:var(--taupe);font-weight:500}
.brand-mark{position:absolute;left:585px;top:48px;width:30px;height:30px;background:var(--taupe)}
.call{position:absolute;left:160px;top:70px;font-size:14px;line-height:24px}
.call span{color:#777}
.search{position:absolute;left:756px;top:79px;width:230px;height:38px;border:2px solid var(--taupe);border-radius:20px;font-size:13px;color:#999;padding:10px 16px}
.search-btn{position:absolute;left:946px;top:83px;width:34px;height:30px;border-radius:15px;background:var(--taupe)}
.icon-round{position:absolute;top:81px;width:34px;height:34px;border-radius:50%;background:#cfc7c0;display:flex;align-items:center;justify-content:center}

.nav{position:absolute;left:0;top:139px;width:1200px;height:54px;background:var(--ink);display:flex;align-items:center;padding-left:112px}
.nav a{color:var(--white);text-decoration:none;font-size:17px;font-weight:500;margin-right:49px}
.nav a.active{font-weight:700;border-bottom:2px solid var(--white);padding-bottom:3px}

.hero{position:absolute;left:0;top:193px;width:1200px;height:519px;background:linear-gradient(90deg,#f4f4f6 0%,#e9e9ec 60%,#dcdde2 100%)}
.hero-photo{left:640px;top:0;width:560px;height:519px;background:radial-gradient(ellipse at 55% 50%,#3a7fc0 0%,#9fb2c7 35%,rgba(220,221,226,0) 70%)}
.hero h1{position:absolute;left:102px;top:120px;font-size:46px;line-height:51px;color:var(--navy);letter-spacing:1px}
.hero p{position:absolute;left:103px;top:234px;width:380px;font-size:16px;line-height:24px;color:var(--muted)}

.features{position:absolute;left:0;top:712px;width:1200px;height:107px;background:var(--white);border-bottom:1px solid #eee}
.feat{position:absolute;top:22px;width:330px;height:64px}
.feat h4{position:absolute;left:85px;top:4px;font-family:"Abril Fatface",serif;font-weight:400;font-size:14px}
.feat p{position:absolute;left:85px;top:26px;width:200px;font-size:10px;line-height:14px;color:#444}
.feat svg{position:absolute;left:0;top:0}
.vline{position:absolute;top:726px;width:1px;height:75px;background:#ddd}

.promo-label{position:absolute;font-size:13px}
.promo-title{position:absolute;font-family:"Abril Fatface",serif;font-size:29px;line-height:36px}

.products{position:absolute;left:0;top:1497px;width:1200px;height:1032px;background:var(--pale)}
.section-title{position:absolute;left:0;width:1200px;text-align:center;font-family:"Abril Fatface",serif;font-size:31px;color:var(--navy);letter-spacing:.5px}
.card{position:absolute;width:224px;height:322px;background:var(--white)}
.card .pimg{position:absolute;left:42px;top:28px;width:140px;height:170px;border-radius:6px}
.card h5{position:absolute;left:0;top:222px;width:224px;text-align:center;font-family:"Abril Fatface",serif;font-weight:400;font-size:17px}
.card .price{position:absolute;left:0;top:250px;width:224px;text-align:center;font-family:"Abril Fatface",serif;font-size:18px}
.card .stars{position:absolute;left:0;top:277px;width:224px;text-align:center;color:var(--star);font-size:12px;letter-spacing:6px}
.tag{position:absolute;left:10px;top:12px;height:20px;padding:0 8px;font-size:11px;font-weight:700;color:var(--white);display:flex;align-items:center;border-radius:2px}
.tag.new{background:#2e7d32}
.tag.sale{background:var(--navy)}

.sports{position:absolute;left:0;top:2529px;width:1200px;height:493px;background:linear-gradient(90deg,#0f1822 0%,#1c2a38 45%,#2e3c4a 65%,#1d2630 100%)}
.sports h3{position:absolute;left:103px;font-family:"Abril Fatface",serif;font-weight:400;color:var(--white)}

.avatar{position:absolute;left:563px;top:3156px;width:91px;height:91px;border-radius:50%;background:radial-gradient(circle at 50% 40%,#e06a4a,#b94a2e 60%,#c9b8a0)}
.quote{position:absolute;left:190px;top:3271px;width:820px;text-align:center;font-size:14.5px;line-height:22px;color:#333}

.about{position:absolute;left:0;top:3463px;width:1200px;height:554px;background:var(--pale)}
.about-brand{position:absolute;left:100px;top:230px;width:470px;text-align:center;font-size:58px;font-weight:700;color:var(--ink);letter-spacing:2px}
.about h2{position:absolute;left:640px;top:100px;font-family:"Abril Fatface",serif;font-weight:400;font-size:27px;color:var(--navy)}
.about .lead{position:absolute;left:640px;top:145px;width:456px;font-size:13.5px;line-height:22px;font-weight:700;color:#333}
.about .body{position:absolute;left:640px;top:248px;width:456px;font-size:13.5px;line-height:22px;color:#666;text-align:justify}

.footer{position:absolute;left:0;top:4017px;width:1200px;height:288px;background:var(--taupe);color:var(--white)}
.footer h6{position:absolute;top:40px;font-family:"Abril Fatface",serif;font-weight:400;font-size:21px}
.footer ul{position:absolute;top:82px;list-style:none;font-size:13.5px;line-height:22.5px}
.footer .email{position:absolute;left:793px;top:88px;width:246px;height:38px;border:1.5px solid var(--white);border-radius:6px;font-size:12px;padding:11px 12px}
.footer .send{position:absolute;left:1045px;top:91px;width:50px;height:34px;background:var(--white);border-radius:6px;display:flex;align-items:center;justify-content:center}
.fsocial{position:absolute;top:160px;width:26px;height:26px;border-radius:50%;background:var(--white)}
.copy{position:absolute;left:0;top:4305px;width:1200px;height:62px;background:var(--ink);color:var(--white);font-size:14.5px;display:flex;align-items:center;justify-content:center}
.pay{position:absolute;top:4327px;width:26px;height:17px;border-radius:2px}
</style>
</head>
<body>

<div class="topbar">
  <div class="social" style="left:105px" aria-label="Social link"></div>
  <div class="social" style="left:140px" aria-label="Social link"></div>
  <div class="social" style="left:173px" aria-label="Social link"></div>
  <div class="social" style="left:207px" aria-label="Social link"></div>
  <div class="account">
    <svg width="12" height="13" viewBox="0 0 12 13"><circle cx="6" cy="3.5" r="3" fill="#fff"/><path d="M0 13c0-4 2.5-5.5 6-5.5S12 9 12 13z" fill="#fff"/></svg>
    My Account
    <svg width="9" height="6" viewBox="0 0 9 6"><path d="M1 1l3.5 3.5L8 1" stroke="#fff" stroke-width="1.5" fill="none"/></svg>
  </div>
</div>

<div class="header"></div>
<div class="logo-tab"></div>
<div class="brand-mark" aria-hidden="true"></div>
<div class="brand">ORBITWREN</div>
<svg class="abs" style="left:102px;top:78px" width="36" height="36" viewBox="0 0 36 36"><circle cx="18" cy="18" r="16" fill="none" stroke="#999" stroke-width="2"/><path d="M11 10c-1 5 3 12 10 16l3-3-4-3-2 2c-2-1-4-4-4-6l2-2-3-4z" fill="#999"/></svg>
<div class="call"><span>Call Us:</span><br>+1 555 014 2270</div>
<div class="search">Search</div>
<div class="search-btn"></div>
<svg class="abs" style="left:956px;top:90px" width="15" height="15" viewBox="0 0 15 15"><circle cx="6" cy="6" r="4.5" stroke="#fff" stroke-width="2" fill="none"/><path d="M9.5 9.5L14 14" stroke="#fff" stroke-width="2"/></svg>
<div class="icon-round" style="left:1009px"><svg width="14" height="12" viewBox="0 0 14 12"><path d="M7 12L1 6a3 3 0 015-4l1 1 1-1a3 3 0 015 4z" fill="#333"/></svg></div>
<div class="icon-round" style="left:1060px"><svg width="16" height="14" viewBox="0 0 16 14"><path d="M1 5h14l-2 8H3z" fill="none" stroke="#333" stroke-width="1.6"/><path d="M4 5l4-4 4 4" fill="none" stroke="#333" stroke-width="1.6"/></svg></div>

<nav class="nav">
  <a class="active">Home</a><a>About Us</a><a>New Collection</a><a>New Arrivals</a><a>Sale</a><a>Menswear</a><a>Latest Blog</a><a>Contact Us</a>
</nav>

<section class="hero">
  <div class="ph hero-photo" role="img" aria-label="Young boy in a blue and white tracksuit and white trainers striking a dance pose"></div>
  <h1 class="serif">YOUNG BOYS<br>COLLECTION</h1>
  <p>Lorem ipsum dolor sit amet, consectetur adipiscing elit, sed do eiusmod tempor incididunt ut labore et dolore magna aliqua.</p>
  <div class="btn" style="left:104px;top:327px;width:141px;height:41px">SHOP NOW</div>
</section>

<div class="features">
  <div class="feat" style="left:100px">
    <svg width="64" height="50" viewBox="0 0 64 50"><rect x="2" y="10" width="36" height="26" fill="none" stroke="#888" stroke-width="2"/><path d="M38 18h14l8 10v8H38z" fill="none" stroke="#888" stroke-width="2"/><circle cx="14" cy="40" r="5" fill="#fff" stroke="#888" stroke-width="2"/><circle cx="48" cy="40" r="5" fill="#fff" stroke="#888" stroke-width="2"/><path d="M13 23l5 5 9-9" fill="none" stroke="#888" stroke-width="2"/></svg>
    <h4>FREE SHIPPING</h4>
    <p>Lorem ipsum dolor sit amet, consectetur adipiscing elit, incididunt ut aliqua.</p>
  </div>
  <div class="feat" style="left:480px">
    <svg width="50" height="50" viewBox="0 0 50 50"><circle cx="25" cy="25" r="21" fill="none" stroke="#888" stroke-width="2"/><path d="M14 20l11-6 11 6v12l-11 6-11-6z" fill="none" stroke="#888" stroke-width="2"/><path d="M14 20l11 6 11-6M25 26v12" fill="none" stroke="#888" stroke-width="2"/></svg>
    <h4>30 DAYS RETURN</h4>
    <p>Lorem ipsum dolor sit amet, consectetur adipiscing elit, incididunt ut aliqua.</p>
  </div>
  <div class="feat" style="left:840px">
    <svg width="50" height="50" viewBox="0 0 50 50"><path d="M25 4l18 7v12c0 12-8 20-18 24C15 43 7 35 7 23V11z" fill="none" stroke="#888" stroke-width="2"/><path d="M17 25l6 6 11-12" fill="none" stroke="#888" stroke-width="2"/></svg>
    <h4>100% PAYMENT SECURE</h4>
    <p>Lorem ipsum dolor sit amet, consectetur adipiscing elit, incididunt ut aliqua.</p>
  </div>
</div>
<div class="vline" style="left:424px"></div>
<div class="vline" style="left:786px"></div>

<div class="ph" style="left:24px;top:883px;width:379px;height:271px;background:var(--yellow)"></div>
<div class="ph" style="left:225px;top:895px;width:150px;height:259px;background:radial-gradient(ellipse at 50% 50%,#4f6e98 0%,#f3e6c8 55%,rgba(240,179,35,0) 75%)" role="img" aria-label="Boy in a denim shirt and white shorts"></div>
<div class="promo-label" style="left:64px;top:944px">For Boys Online</div>
<div class="promo-title" style="left:58px;top:968px">Athleisure<br>Products</div>
<div class="btn" style="left:57px;top:1051px;width:117px;height:38px">SHOP NOW</div>

<div class="ph" style="left:415px;top:883px;width:371px;height:271px;background:var(--slate)"></div>
<div class="ph" style="left:600px;top:935px;width:165px;height:160px;background:radial-gradient(ellipse at 50% 55%,#151826 0%,#232638 55%,rgba(42,45,62,0) 75%)" role="img" aria-label="Navy baseball cap"></div>
<div class="promo-label" style="left:448px;top:944px;color:#fff">Boys Cap</div>
<div class="promo-title" style="left:448px;top:968px;color:#fff">Boys<br>Cap</div>
<div class="btn" style="left:446px;top:1051px;width:118px;height:38px">SHOP NOW</div>

<div class="ph" style="left:800px;top:883px;width:373px;height:554px;background:linear-gradient(180deg,#c3ccd4 0%,#d7dde2 30%,#cfd5dc 100%)"></div>
<div class="ph" style="left:800px;top:1033px;width:373px;height:404px;background:radial-gradient(ellipse at 55% 60%,#d6382e 0%,#6a5c6b 35%,rgba(207,213,220,0) 65%)" role="img" aria-label="Smiling boy in a red sports kit holding a football"></div>
<div class="promo-label" style="left:824px;top:906px;color:#fff">Collection Of 2023</div>
<div class="promo-title" style="left:824px;top:926px;color:#fff;font-size:26px">Boys Sports Outfits</div>
<div class="btn" style="left:824px;top:979px;width:117px;height:38px">SHOP NOW</div>

<div class="ph" style="left:24px;top:1166px;width:762px;height:271px;background:linear-gradient(90deg,#9a9a92 0%,#b6b4a8 45%,#8f8c80 100%)" role="img" aria-label="Boy in a cap and vest sitting cross-legged against a textured grey wall"></div>
<div class="promo-title" style="left:440px;top:1196px;width:254px;text-align:right;color:#fff;font-size:34px;line-height:42px">Athleisure<br>Dress</div>
<div class="abs" style="left:380px;top:1288px;width:318px;text-align:right;color:#fff;font-size:12.5px;line-height:19px">Lorem ipsum dolor sit amet, consectetur adipiscing elit, sed do eiusmod tempor incididunt ut labore et dolore magna aliqua.</div>
<div class="btn" style="left:580px;top:1356px;width:117px;height:38px">SHOP NOW</div>

<section class="products">
  <div class="section-title" style="top:115px">FEATURED PRODUCTS</div>

  <div class="card" style="left:103px;top:195px"><div class="pimg" style="background:linear-gradient(180deg,#b5c9e6,#8fa9d0)" role="img" aria-label="Light blue shirt"></div><h5>Shirts</h5><div class="price">$59.00</div><div class="stars">★★★★★</div></div>
  <div class="card" style="left:359px;top:195px"><div class="tag new">NEW</div><div class="pimg" style="background:linear-gradient(180deg,#3a5a93,#22386a)" role="img" aria-label="Navy pants"></div><h5>Pant</h5><div class="price">$59.00</div><div class="stars">★★★★★</div></div>
  <div class="card" style="left:617px;top:195px"><div class="pimg" style="background:linear-gradient(180deg,#2a2a2a,#0d0d0d)" role="img" aria-label="Black track pants"></div><h5>Track Pant</h5><div class="price">$59.00</div><div class="stars">★★★★★</div></div>
  <div class="card" style="left:873px;top:195px"><div class="tag new">NEW</div><div class="pimg" style="background:linear-gradient(180deg,#a9a9a9,#7e7e7e)" role="img" aria-label="Grey sweat pants"></div><h5>Sweat Pants</h5><div class="price">$59.00</div><div class="stars">★★★★★</div></div>

  <div class="card" style="left:103px;top:546px"><div class="pimg" style="background:linear-gradient(180deg,#f4b43a,#e3951c)" role="img" aria-label="Orange hoodie"></div><h5>Hoodies</h5><div class="price">$59.00</div><div class="stars">★★★★★</div></div>
  <div class="card" style="left:359px;top:546px"><div class="pimg" style="background:linear-gradient(180deg,#25408f,#14275f)" role="img" aria-label="Blue zip jacket"></div><h5>Jackets</h5><div class="price">$59.00</div><div class="stars">★★★★★</div></div>
  <div class="card" style="left:617px;top:546px;height:361px;box-shadow:0 4px 16px rgba(0,0,0,.15)">
    <div class="tag sale">-17</div>
    <div class="pimg" style="top:20px;height:160px;background:linear-gradient(180deg,#8fb0d6,#5f86b6)" role="img" aria-label="Denim jacket"></div>
    <svg class="abs" style="left:186px;top:16px" width="28" height="28" viewBox="0 0 28 28"><circle cx="14" cy="14" r="13" fill="#111"/><path d="M14 20l-5-5a2.6 2.6 0 014-3.4l1 1 1-1a2.6 2.6 0 014 3.4z" fill="#fff"/></svg>
    <svg class="abs" style="left:186px;top:54px" width="28" height="28" viewBox="0 0 28 28"><circle cx="14" cy="14" r="13" fill="#111"/><path d="M8 12h12l-2 7h-8z" fill="none" stroke="#fff" stroke-width="1.5"/><path d="M11 12l3-3 3 3" fill="none" stroke="#fff" stroke-width="1.5"/></svg>
    <h5 style="top:205px">Jean Jacket</h5><div class="price" style="top:233px">$59.00</div><div class="stars" style="top:260px">★★★★★</div>
    <div class="btn" style="left:41px;top:295px;width:141px;height:43px">SHOP NOW</div>
  </div>
  <div class="card" style="left:873px;top:546px"><div class="pimg" style="background:linear-gradient(180deg,#8eb5e0,#5e8cc6)" role="img" aria-label="Denim shorts"></div><h5>Shirts</h5><div class="price">$59.00</div><div class="stars">★★★★★</div></div>
</section>

<section class="sports">
  <div class="ph" style="left:560px;top:0;width:560px;height:493px;background:radial-gradient(ellipse at 50% 55%,#6d6a66 0%,#3b4550 40%,rgba(29,38,48,0) 75%)" role="img" aria-label="Teenage athlete in a sleeveless kit resting with hands on knees in a gym"></div>
  <h3 style="top:80px;font-size:36px">SPORTS OUTFITS</h3>
  <h3 style="top:146px;font-size:33px">WEEKEND SALE</h3>
  <h3 style="top:206px;font-size:62px">UP TO 50% OFF</h3>
  <div class="abs" style="left:103px;top:297px;width:143px;height:45px;border:2px solid #fff;color:#fff;font-family:'Abril Fatface',serif;font-size:15px;display:flex;align-items:center;justify-content:center">SHOP NOW</div>
</section>

<div class="section-title" style="top:3078px">WHAT PEOPLE SAY</div>
<div class="avatar" role="img" aria-label="Customer portrait"></div>
<p class="quote">Lorem ipsum dolor sit amet, consectetur adipiscing elit, sed do eiusmod tempor incididunt ut labore et dolore magna aliqua. Ut enim ad minim veniam, quis nostrud exercitation ullamco laboris nisi ut aliquip ex ea commodo consequat. Duis aute irure dolor in reprehenderit in voluptate velit esse cillum dolore eu fugiat nulla pariatur.</p>
<div class="abs" style="left:0;top:3347px;width:1200px;text-align:center;font-size:17px;font-weight:500">– Kai Morgan</div>
<div class="abs" style="left:0;top:3373px;width:1200px;text-align:center;font-size:14px;color:#444">( Customer)</div>

<section class="about">
  <div class="about-brand">ORBITWREN</div>
  <h2>ABOUT ORBITWREN</h2>
  <p class="lead">Lorem ipsum dolor sit amet, consectetur adipiscing elit, sed do eiusmod tempor incididunt ut labore et dolore magna aliqua. Ut enim ad minim veniam, quis nostrud exercitation ullamco laboris nisi ut aliquip ex ea commodo consequat.</p>
  <p class="body">Sed ut perspiciatis unde omnis iste natus error sit voluptatem accusantium doloremque laudantium, totam rem aperiam, eaque ipsa quae ab illo inventore veritatis et quasi architecto beatae vitae dicta sunt explicabo. Nemo enim ipsam voluptatem quia voluptas sit aspernatur aut odit aut fugit, sed quia consequuntur magni dolores eos qui ratione voluptatem sequi nesciunt. Neque porro quisquam est, qui dolorem ipsum quia dolor sit amet,</p>
  <div class="btn" style="left:640px;top:410px;width:141px;height:41px">RAED MORE</div>
</section>

<footer class="footer">
  <h6 style="left:108px">Quick Link</h6>
  <ul style="left:108px"><li>Home</li><li>About Us</li><li>New Collection</li><li>New Arrivals</li><li>Sale</li><li>Menswear</li><li>Latest Blog</li><li>Contact Us</li></ul>
  <h6 style="left:330px">Help Links</h6>
  <ul style="left:330px"><li>Search</li><li>About Us</li><li>Delivery</li><li>Our stores</li></ul>
  <h6 style="left:529px">Contact Us</h6>
  <ul style="left:529px;font-size:12.5px;line-height:21px"><li>58N Lorem ipsum dolor sit amet,</li><li>consectetur adipiscing elit</li><li style="margin-top:7px">info@orbitwren.com</li><li style="margin-top:7px">+1 555 014 2270</li></ul>
  <h6 style="left:793px">Newsletter</h6>
  <div class="email">Enter Email</div>
  <div class="send"><svg width="16" height="16" viewBox="0 0 16 16"><path d="M1 7l14-6-5 14-2-6z" fill="#333"/></svg></div>
  <div class="fsocial" style="left:794px" aria-label="Social link"></div>
  <div class="fsocial" style="left:834px" aria-label="Social link"></div>
  <div class="fsocial" style="left:875px" aria-label="Social link"></div>
</footer>
<div class="copy">© Copyright 2023 Orbit Wren | All rights reserved</div>
<div class="pay" style="left:900px;background:#555"></div>
<div class="pay" style="left:931px;background:#ddd"></div>
<div class="pay" style="left:962px;background:#eee"></div>
<div class="pay" style="left:993px;background:#bbb"></div>
<div class="pay" style="left:1024px;background:#4a79c4"></div>
<div class="pay" style="left:1055px;background:#888"></div>

</body>
</html>
```